Vantor Health Group Presentation Folder, for Cancer Awareness, VERY COLORFUL AND MODERN

Presentation Folder I know pretty much what i want so it should be very eazy , I have included files from folders I use now rebrand them to my new company they will be fine, no sense re creating the wheel
Full Bleed Size
20.87" x 16.68"
53 x 42.4 cm
6260 x 5004 pixels
Document Trim Size
20.75" x 16.56"
52.7 x 42.1 cm
6225 x 4969 pixels
Updates

Low design quality

Industry/Entity Type

Medical

Font styles to use
Serif

Colors

Designer to choose colors to be used in the design.

Requirements
Must have
• really I am not looking for some one to redesign, we like our folder front page and would like to see new word information added., there are two folder front pages to choose from
• So Keep the original front page and redesign the back page and the pockets
• Can Make your Design off of one of the ones I already uploaded
Nice to have
• Keep the same color schemes, Keep the original front page and redesign the back page and the pockets
Should not have
• DO not recreate the front covers, use what I gave you and just rebrand

```html
<!DOCTYPE html>
<html lang="en">
<head>
<meta charset="utf-8">
<title>Vantor Health Group – Hereditary Cancer Screening Folder</title>
<link href="https://fonts.googleapis.com/css2?family=Raleway:wght@300;400;500;600;700&display=swap" rel="stylesheet">
<style>
  :root{
    --pink:#f497a8;
    --grey:#6d6e71;
    --grey-mid:#8b8c8f;
    --grey-flap:#a0a1a4;
    --grey-light:#d1d3d4;
    --die:#e4312f;
    --white:#ffffff;
    --ink:#4d4d4f;
    --navy:#1f3f73;
    --ribbon-blue:#3a6fb0;
    --ribbon-pink:#f4b6c6;
  }
  html,body{margin:0;padding:0;width:1200px;height:1200px;overflow:hidden;background:var(--white);}
  body{font-family:"Raleway",sans-serif;}
  .sheet{position:relative;width:1250px;height:1250px;transform:scale(.96);transform-origin:0 0;}
  .abs{position:absolute;}
  .dieline{position:absolute;left:0;top:0;}
  .band-pink{background:var(--pink);}
  .band-grey{background:var(--grey);}
  .fold-line{position:absolute;left:625px;top:162px;width:0;height:698px;border-left:1px dashed #9a9a9a;}

  .intro-box{left:101px;top:243px;width:486px;height:151px;border:1px solid var(--white);box-sizing:border-box;padding:17px 10px 0 14px;
    color:var(--white);font-size:11.4px;letter-spacing:1.55px;line-height:14.9px;text-transform:uppercase;font-weight:400;}

  .photo-beach{left:67px;top:410px;width:558px;height:340px;
    background:
      radial-gradient(ellipse 60% 45% at 70% 30%, rgba(255,255,255,.55), rgba(255,255,255,0) 70%),
      linear-gradient(180deg,#e4e4e4 0%,#cfcfcf 35%,#a9a9a9 55%,#8a8a8a 70%,#6b6b6b 85%,#585858 100%);}
  .photo-table{left:627px;top:395px;width:556px;height:355px;
    background:
      radial-gradient(ellipse 55% 40% at 25% 15%, rgba(255,255,255,.7), rgba(255,255,255,0) 70%),
      radial-gradient(ellipse 50% 35% at 60% 70%, rgba(240,240,240,.45), rgba(240,240,240,0) 70%),
      linear-gradient(165deg,#f0f0f0 0%,#cfcfcf 35%,#a4a4a4 65%,#7c7c7c 100%);}
  .caption{left:112px;top:663px;width:472px;height:87px;background:rgba(70,70,70,.5);color:var(--white);
    text-align:center;font-size:12.2px;letter-spacing:1.55px;line-height:15.6px;text-transform:uppercase;font-weight:500;padding-top:9px;box-sizing:border-box;}

  .title{left:627px;top:226px;width:556px;height:47px;color:var(--white);font-size:21px;letter-spacing:3.4px;
    font-weight:400;text-align:center;line-height:51px;}
  .tagline{left:627px;top:273px;width:556px;height:37px;background:var(--grey-mid);color:var(--white);font-size:12.5px;
    letter-spacing:1.3px;line-height:37px;text-align:center;font-weight:300;}
  .ribbon{left:1112px;top:270px;width:20px;height:36px;background:linear-gradient(90deg,var(--ribbon-blue) 50%,var(--ribbon-pink) 50%);border-radius:8px 8px 2px 2px;transform:rotate(-12deg);}
  .lede{left:627px;top:335px;width:556px;color:var(--ink);font-size:13.4px;letter-spacing:1.3px;line-height:16px;text-align:center;font-weight:400;}

  .order-line{left:752px;top:773px;color:var(--white);font-size:12.5px;letter-spacing:1.6px;font-weight:400;}
  .brand-dot{left:686px;top:776px;width:45px;height:45px;border-radius:50%;background:var(--white);border:3px solid var(--navy);box-sizing:border-box;}

  .flip{transform:rotate(180deg);}
  .imprint{left:196px;top:868px;width:340px;height:44px;display:flex;align-items:center;gap:40px;}
  .imprint-mark{width:58px;height:38px;background:var(--white);flex:none;}
  .imprint-name{color:var(--white);font-size:16.5px;letter-spacing:2px;font-weight:700;line-height:20px;}
  .imprint-sub{color:var(--white);font-size:11px;letter-spacing:1.4px;font-weight:400;}

  .pocket-copy{left:700px;top:887px;width:403px;height:192px;color:var(--white);display:flex;flex-direction:column;}
  .pocket-head{font-size:10.5px;letter-spacing:1.55px;font-weight:600;text-transform:uppercase;white-space:nowrap;}
  .pocket-sub{font-size:6.3px;letter-spacing:.9px;font-weight:700;text-transform:uppercase;margin:3px 0 0 60px;}
  .pocket-rule{height:1px;background:var(--white);margin:10px 0 14px;}
  .pocket-body{font-size:8.1px;letter-spacing:.85px;line-height:10.1px;margin:0;}
  .pocket-body + .pocket-body{margin-top:auto;}
</style>
</head>
<body>
<div class="sheet">

  <svg class="dieline" width="1250" height="1250" viewBox="0 0 1250 1250">
    <defs>
      <clipPath id="pocket-left"><path d="M70 860 L620 860 L586 1088 Q580 1123 548 1123 L70 1123 Z"/></clipPath>
      <clipPath id="pocket-right"><path d="M630 860 L1180 860 L1180 1123 L702 1123 Q670 1123 665 1088 Z"/></clipPath>
    </defs>
    <rect x="67" y="162" width="1116" height="53" fill="var(--grey-flap)"/>
    <path d="M67 162 L22 168 L22 580 A20 20 0 0 1 22 620 L22 850 L67 860 Z" fill="var(--grey-flap)" stroke="var(--die)" stroke-width="1"/>
    <path d="M1183 162 L1228 168 L1228 580 A20 20 0 0 0 1228 620 L1228 850 L1183 860 Z" fill="var(--grey-flap)" stroke="var(--die)" stroke-width="1"/>
    <line x1="67" y1="162" x2="1183" y2="162" stroke="var(--die)"/>

    <g clip-path="url(#pocket-left)">
      <rect x="70" y="860" width="550" height="263" fill="var(--pink)"/>
      <rect x="70" y="860" width="38" height="263" fill="var(--grey-light)"/>
      <rect x="108" y="860" width="512" height="60" fill="var(--grey)"/>
    </g>
    <path d="M70 860 L70 1123 L548 1123 Q580 1123 586 1088 L620 860" fill="none" stroke="var(--die)"/>
    <g stroke="var(--grey)" stroke-width="1">
      <line x1="240" y1="966" x2="276" y2="930"/>
      <line x1="414" y1="930" x2="450" y2="966"/>
      <line x1="240" y1="1018" x2="276" y2="1054"/>
      <line x1="414" y1="1054" x2="450" y2="1018" stroke="var(--die)"/>
    </g>

    <g clip-path="url(#pocket-right)">
      <rect x="630" y="860" width="550" height="263" fill="var(--pink)"/>
      <rect x="1143" y="860" width="37" height="263" fill="var(--grey-light)"/>
      <rect x="630" y="860" width="513" height="60" fill="var(--grey)"/>
    </g>
    <path d="M630 860 L665 1088 Q670 1123 702 1123 L1180 1123 L1180 860" fill="none" stroke="var(--die)"/>
    <line x1="67" y1="860" x2="1183" y2="860" stroke="#3aa657" stroke-dasharray="3 2" stroke-width=".8"/>
  </svg>

  <!-- back cover -->
  <div class="abs band-pink" style="left:67px;top:226px;width:558px;height:184px;"></div>
  <div class="abs intro-box">Hereditary cancer screening provides vital information to help people with a strong personal or family history of cancer understand their own risk of developing the disease.<br>With this information, they can take steps to potentially prevent cancer, delay the onset of cancer or catch it at an earlier stage when outcomes and survival rates are better.</div>
  <div class="abs photo-beach" role="img" aria-label="Black and white photo of a multi-generation family holding hands on a rocky seashore, seen from behind"></div>
  <div class="abs caption">Don't be afraid of the answer: knowledge is power<br>and power eradicates fear.<br>When you are fearless, you will make all<br>the right choices!</div>

  <!-- front cover -->
  <div class="abs band-pink title">HEREDITARY CANCER SCREENING</div>
  <div class="abs tagline">DOCTORS ARE THE GATEKEEPERS TO GENETIC TESTING</div>
  <div class="abs ribbon" role="img" aria-label="Awareness ribbon in blue and pink"></div>
  <div class="abs lede">We have an obligation to help patients understand genetic risk<br>and how testing can guide heath care decisions</div>
  <div class="abs photo-table" role="img" aria-label="Black and white photo of a family sharing a meal at an outdoor table"></div>

  <!-- lower bands -->
  <div class="abs band-grey" style="left:67px;top:758px;width:1116px;height:42px;"></div>
  <div class="abs band-pink" style="left:67px;top:800px;width:1116px;height:60px;"></div>
  <div class="abs brand-dot"></div>
  <div class="abs order-line">THE TEST YOU ORDER FOR YOUR PATIENTS</div>
  <div class="fold-line"></div>

  <!-- left pocket imprint -->
  <div class="abs imprint flip">
    <div class="imprint-mark"></div>
    <div>
      <div class="imprint-name">Vantor Health Group</div>
      <div class="imprint-sub">a division of Meridian Clinical Sales LLC</div>
    </div>
  </div>

  <!-- right pocket copy -->
  <div class="abs pocket-copy flip">
    <div class="pocket-head">Identifying an inherited genetic mutation has</div>
    <div class="pocket-sub">The potential to prevent cancer and save lives</div>
    <div class="pocket-rule"></div>
    <p class="pocket-body">There are many benefits to getting tested, regardless of the eventual result. If one of your family members – however distant – had cancer, there is a chance that you inherited a gene mutation that not only increases your personal risk of cancer, but also could be passed to the next generation. Those who are carriers of hereditary cancer gene mutations could be at risk of getting cancer earlier in life than the general population. The sooner genetic testing is done, the more likely it is that the risk can be managed appropriately.</p>
    <p class="pocket-body">Hereditary cancer screening provides vital information to help people with a strong personal or family history of cancer understand their own risk of developing the disease. With this information, they can take steps to Potentially Prevent Cancer, Delay the Onset of Cancer or Catch it at an Earlier stage when outcomes and survival rates are Better.</p>
  </div>

</div>
</body>
</html>
```